Warehouse Surplus Flyer

2 Sided Flyer to be used in print and online for short, unadvertised sale to pharmacies for prescription vials. Please feel free to edit wordiness.

Side One:
WE PASS ALONG THE SAVINGS TO YOU
WAREHOUSE SURPLUS UNADVERTISED OFFER
BY INVITATION ONLY TO YOU

We have a acquired a surplus, with our supplier, on ALL AMBER color and ALL with CHILD RESISTANT CAPS and we would like to pass along the savings to you, as we need to make room for other inventory.

Normally these vials sell for over $50 a case! We are going to move these vials at very special pricing.

Very cost-effective, Quality Vials

Korvel Supply provides pharmacy vials in the independent pharmacy market and conditioned toner cartridges in pharmacies and several other vertical markets.
Please call us at 877-412-5960 and we will be happy to work with you directly.

korvelsupply.example

This is not an advertised sale. Offer Ends September 30, 2013*.

2nd Side:
VIAL SIZE QUANTITY PER CASE CASES AVAILABLE
8 Dram 410 50
10 Dram 360 50
13 Dram 310 500
16 Dram 260 500
20 Dram 270 500
30 Dram 240 500
40 Dram 200 500
60 Dram 140 100

During this offer to move inventory, we are selling these at 30% to 50% off our already discounted rate, based on volume.

Quantities: (*While Supplies Last)
• 1 to 500 cases will be sold at 30% off our discounted price! $28 Per Case
• 501 to 1000 cases will be sold at 40% our discounted price! $25 Per Case
• Over 1000 cases will be sold at 50% our discounted price! $22 Per Case

We also have great pricing on conditioned toner cartridges. You can also view our line of products and prices on www.korvelsupply.example.

Please call us at 877-412-5960 and we will be happy to work with you directly. This is not an advertised sale.
Updates

Deadline IS AUGUST 28TH! SEPTEMBER SALE.

Target Market(s)

Independent Pharmacies

Industry/Entity Type

Online

Requirements
Must have
• 3 color or Less front side, 2 Sided Flyer
• Backside can be 1 Color
• Phone Number
• web address
• sales expiration date
Nice to have
• graphic call outs to gain attention

```html
<!DOCTYPE html>
<html lang="en">
<head>
<meta charset="utf-8">
<title>Korvel Supply – Warehouse Surplus Pricing</title>
<link href="https://fonts.googleapis.com/css2?family=Ribeye&family=Arimo:wght@700&display=swap" rel="stylesheet">
<style>
  :root {
    --ink-blue: #2330c8;
    --table-yellow: #ffff00;
    --table-border: #1f2fd0;
    --rule-black: #111111;
    --bg-white: #ffffff;
    --bg-mint: #b6f7a0;
    --bg-green: #3cf21c;
    --card-white: #ffffff;
  }
  html, body {
    margin: 0;
    padding: 0;
    width: 927px;
    height: 1200px;
    overflow: hidden;
  }
  .flyer {
    position: relative;
    width: 927px;
    height: 1200px;
    background: linear-gradient(90deg, var(--bg-white) 0%, var(--bg-mint) 45%, var(--bg-green) 100%);
    font-family: "Ribeye", "Trebuchet MS", sans-serif;
    color: var(--ink-blue);
    font-variant: small-caps;
  }
  .inventory-table {
    position: absolute;
    left: 56px;
    top: 56px;
    width: 816px;
    border-collapse: collapse;
    border: 3px solid var(--table-border);
    background: var(--table-yellow);
  }
  .inventory-table th,
  .inventory-table td {
    border: 1.5px solid var(--rule-black);
    text-align: center;
    height: 26px;
    padding: 0;
    width: 33.33%;
  }
  .inventory-table th {
    font-family: "Ribeye", "Trebuchet MS", sans-serif;
    font-size: 20px;
    font-weight: 400;
    color: var(--ink-blue);
    font-variant: small-caps;
    text-transform: uppercase;
    letter-spacing: 0.5px;
  }
  .inventory-table td {
    font-family: "Arimo", Arial, sans-serif;
    font-weight: 700;
    font-size: 19px;
    font-variant: normal;
    color: var(--ink-blue);
  }
  .offer-intro {
    position: absolute;
    left: 59px;
    top: 333px;
    width: 820px;
    margin: 0;
    font-size: 19.5px;
    line-height: 26px;
  }
  .quantities-title {
    position: absolute;
    left: 59px;
    top: 418px;
    margin: 0;
    font-size: 26px;
    font-weight: 400;
  }
  .supply-note {
    position: absolute;
    left: 59px;
    top: 450px;
    margin: 0;
    font-size: 18px;
  }
  .tier {
    position: absolute;
    left: 59px;
    margin: 0;
    font-size: 20px;
  }
  .tier-one { top: 500px; }
  .tier-two { top: 583px; }
  .tier-three { top: 666px; }
  .price-tag {
    position: absolute;
    left: 55px;
    height: 34px;
    line-height: 34px;
    padding: 0 12px 0 8px;
    background: var(--table-yellow);
    font-size: 27px;
    letter-spacing: 1px;
  }
  .price-one { top: 528px; width: 253px; box-sizing: border-box; }
  .price-two { top: 612px; width: 212px; box-sizing: border-box; }
  .price-three { top: 697px; width: 218px; box-sizing: border-box; }
  .toner-note {
    position: absolute;
    left: 59px;
    top: 778px;
    width: 820px;
    margin: 0;
    font-size: 19.5px;
    line-height: 26px;
  }
  .web-address {
    position: absolute;
    left: 0;
    top: 857px;
    width: 927px;
    text-align: center;
    margin: 0;
    font-size: 24px;
    letter-spacing: 1px;
    text-transform: uppercase;
    font-variant: normal;
  }
  .brand-card {
    position: absolute;
    left: 343px;
    top: 920px;
    width: 241px;
    height: 262px;
    box-sizing: border-box;
    border: 6px solid var(--table-border);
    background: var(--card-white);
    display: flex;
    align-items: flex-end;
    justify-content: center;
    padding-bottom: 18px;
  }
  .brand-name {
    font-size: 30px;
    color: var(--ink-blue);
    white-space: nowrap;
  }
</style>
</head>
<body>
<main class="flyer">
  <table class="inventory-table">
    <thead>
      <tr><th>Vial Size</th><th>Quantity per Case</th><th>Cases Available</th></tr>
    </thead>
    <tbody>
      <tr><td>8 Dram</td><td>410</td><td>50</td></tr>
      <tr><td>10 Dram</td><td>360</td><td>50</td></tr>
      <tr><td>13 Dram</td><td>310</td><td>500</td></tr>
      <tr><td>16 Dram</td><td>260</td><td>500</td></tr>
      <tr><td>20 Dram</td><td>270</td><td>500</td></tr>
      <tr><td>30 Dram</td><td>240</td><td>500</td></tr>
      <tr><td>40 Dram</td><td>200</td><td>500</td></tr>
      <tr><td>60 Dram</td><td>140</td><td>100</td></tr>
    </tbody>
  </table>

  <p class="offer-intro">During this offer to move inventory, we are selling these at 30% to 50% off our already discounted rate, based on volume.</p>

  <h2 class="quantities-title">Quantities:</h2>
  <p class="supply-note">(*While Supplies Last)</p>

  <p class="tier tier-one">• 1 to 500 cases will be sold at 30% off our discounted price!</p>
  <div class="price-tag price-one">$28 Per Case</div>

  <p class="tier tier-two">• 501 to 1000 cases will be sold at 40% our discounted price!</p>
  <div class="price-tag price-two">$25 Per Case</div>

  <p class="tier tier-three">• Over 1000 cases will be sold at 50% our discounted price!</p>
  <div class="price-tag price-three">$22 Per Case</div>

  <p class="toner-note">We also have great pricing on conditioned toner cartridges.<br>You can also view our line of products and prices on</p>

  <p class="web-address">www.korvelsupply.example</p>

  <div class="brand-card">
    <span class="brand-name">Korvel Supply</span>
  </div>
</main>
</body>
</html>
```